Debt Relief Landing Page Design

I need a landing page designed (and the accompanying Thank You page) for my client.

I have drafted the wireframes for the layout of the pages (attached) and need a professional looking finish.

The main colours to use are green and blue as per their current branding, see website for specifications - http://www.clearpathledger.com.au/

```html
<!DOCTYPE html>
<html lang="en">
<head>
<meta charset="utf-8">
<title>ClearPath Ledger – Debt Relief</title>
<link rel="stylesheet" href="https://fonts.googleapis.com/css2?family=Roboto+Condensed:wght@400;700&family=Roboto+Slab:wght@300;400&family=Open+Sans:wght@400;600&family=Arimo&display=swap">
<style>
:root{
  --navy:#1a3161;
  --navy-deep:#162d5a;
  --green:#5e8f2b;
  --green-light:#6ea132;
  --hero-text:#ffffff;
  --body-text:#333333;
  --grey:#8a8a8a;
  --white:#ffffff;
}
*{margin:0;padding:0;box-sizing:border-box}
html,body{width:728px;height:1200px;overflow:hidden;background:var(--white)}
body{position:relative;font-family:'Open Sans',sans-serif;color:var(--body-text)}
.abs{position:absolute}

/* header */
.site-header{left:0;top:0;width:728px;height:62px;background:var(--white);border-top:1px solid var(--green)}
.brand{left:48px;top:16px;font-family:'Roboto Condensed',sans-serif;font-weight:700;font-size:26px;color:var(--navy);letter-spacing:-.5px;display:flex;align-items:center;gap:8px}
.brand-dot{width:12px;height:12px;border-radius:50%;background:var(--green)}
.call{left:564px;top:22px;display:flex;gap:6px;align-items:center}
.call-label{font-family:'Roboto Slab',serif;font-size:9.5px;color:var(--green);line-height:1}
.call-number{font-family:'Roboto Condensed',sans-serif;font-weight:700;font-size:15px;color:var(--green);line-height:1.1}

/* hero */
.hero{left:0;top:62px;width:728px;height:267px;background:linear-gradient(90deg,#3d3f42 0%,#4a4c4f 40%,#555759 100%)}
.hero-photo{left:0;top:0;width:728px;height:267px;background:radial-gradient(ellipse at 14% 40%,rgba(140,120,100,.45),transparent 38%)}
.hero-shade{left:0;top:0;width:728px;height:267px;background:rgba(40,42,45,.35)}
.hero-title{left:0;top:20px;width:728px;text-align:center;font-family:'Roboto Condensed',sans-serif;font-size:33px;color:var(--green-light)}
.hero-copy{left:40px;top:66px;width:648px;text-align:center;font-family:'Roboto Condensed',sans-serif;font-size:14px;line-height:17.5px;color:var(--hero-text)}
.hero-copy p{margin-bottom:8px}
.btn{display:flex;align-items:center;justify-content:center;font-family:'Roboto Slab',serif;font-size:12.5px;color:var(--white);border:1px solid var(--white);border-radius:2px}
.hero .btn{left:264px;top:220px;width:190px;height:32px;background:var(--green)}

/* services */
.section-title{width:728px;left:0;text-align:center;font-family:'Roboto Slab',serif;font-size:16px;color:var(--navy)}
.section-title em{font-style:normal;color:var(--green)}
.dash{height:0;border-top:1px dashed #999}
.service{width:200px;text-align:center}
.service-icon{width:56px;height:56px;margin:0 auto;display:block}
.service-name{font-family:'Roboto Slab',serif;font-size:11.5px;color:#222;margin-top:10px;height:26px}
.service-text{font-size:10px;line-height:14.3px;color:#444}

/* consultation */
.consult{left:0;top:746px;width:728px;height:192px;background:var(--green);border-top:2px solid #4d7a20}
.consult-title{left:0;top:16px;width:728px;text-align:center;font-family:'Roboto Slab',serif;font-size:15.5px;color:var(--white)}
.consult-sub{left:0;top:44px;width:728px;text-align:center;font-family:'Roboto Slab',serif;font-size:15.5px;color:var(--white)}
.field{height:17px;border:1px solid #d9e6c6;font-family:'Roboto Slab',serif;font-size:8.5px;color:var(--white);padding:2px 6px;width:189px}
.consult .btn{left:270px;top:138px;width:190px;height:32px;background:transparent}

/* testimonials */
.reviews{left:0;top:940px;width:728px;height:225px;background:var(--navy-deep);border-top:2px solid #e0e0e0}
.reviews-title{left:0;top:22px;width:728px;text-align:center;font-family:'Roboto Slab',serif;font-size:16px;color:var(--white)}
.reviews-sub{left:0;top:44px;width:728px;text-align:center;font-family:'Roboto Slab',serif;font-size:11px;color:var(--white)}
.avatar{width:72px;height:72px}
.quote{width:206px;height:86px;background:#233b6b;border:1px solid #2d4676;border-radius:2px;padding:8px 8px 0 8px;font-family:'Arimo',sans-serif;font-size:8.3px;line-height:11.5px;color:var(--white)}
.quote-mark{font-family:Georgia,serif;font-size:24px;color:#8796b3;line-height:14px;float:left;margin-right:4px}
.author{font-family:'Arimo',sans-serif;font-size:10px;color:var(--white)}

/* footer */
.site-footer{left:0;top:1165px;width:728px;height:35px;background:var(--green);display:flex;align-items:center;justify-content:center;font-size:8px;font-weight:600;color:var(--white);gap:6px}
.site-footer .sep{width:1px;height:12px;background:#cfe0b8}
</style>
</head>
<body>

<header class="site-header abs">
  <div class="brand abs"><span class="brand-dot"></span>ClearPath Ledger</div>
  <div class="call abs">
    <svg width="20" height="20" viewBox="0 0 20 20"><circle cx="10" cy="10" r="9" fill="none" stroke="#1a3161" stroke-width="1.4"/><path d="M7 5.5c-1 .8-1.2 2.6.5 5s3.7 3.7 4.8 3.2l1-1-1.8-1.7-1 .7c-.8-.3-1.8-1.3-2.2-2.3l.8-.9L7.6 5z" fill="#1a3161"/></svg>
    <div><div class="call-label">Call Us Today</div><div class="call-number">1300 555 014</div></div>
  </div>
</header>

<section class="hero abs">
  <div class="hero-photo abs" role="img" aria-label="Photo of a smiling man working at a laptop in a bright office"></div>
  <div class="hero-shade abs"></div>
  <h1 class="hero-title abs" style="font-weight:400">Looking to Consolidate Your Debts?</h1>
  <div class="hero-copy abs">
    <p>If you have over $10,000 In Debt, We Can Help you be Debt free in 3-5 Years.</p>
    <p>ClearPath Advisers in Australia’s debt help relief specialists. Through years fo industry experience &amp; knowledge, our team of debt management experts can actively advise you on how to get our of the red, fast.</p>
    <p>At ClearPath Advisers we are able to actively rectify your debt problems by creating simple and affordable payment plans for all debts.</p>
    <p>For a free, no obligation consultation simply fill out the form on the right and we’ll be in contact with you shortly.</p>
  </div>
  <a class="btn abs">GET MY FREE CONSTULATION</a>
</section>

<h2 class="section-title abs" style="top:346px;font-weight:400">Here Are just Some Of Our Debt <em>Relief Services</em></h2>
<div class="dash abs" style="left:193px;top:369px;width:366px"></div>

<div class="service abs" style="left:42px;top:394px">
  <svg class="service-icon" viewBox="0 0 56 56"><circle cx="28" cy="28" r="27" fill="#1a3161" stroke="#cfd6e3" stroke-width="2"/><path d="M27 16a4 4 0 1 1 4 4" fill="none" stroke="#fff" stroke-width="2"/><path d="M28 20l-2 12-4-2-3 3 7 7 10-4 1-8-7-2 1-6z" fill="#fff"/></svg>
  <div class="service-name">Debt Consolidation Loans</div>
  <div class="service-text">Stop Getting hassed by creditors.Let us consolidate your personal debts into an easy repayment plan.</div>
</div>
<div class="service abs" style="left:271px;top:394px">
  <svg class="service-icon" viewBox="0 0 56 56"><circle cx="28" cy="28" r="27" fill="#1a3161" stroke="#cfd6e3" stroke-width="2"/><path d="M14 29l14-13 14 13M18 26v14h20V26" fill="none" stroke="#fff" stroke-width="2.5"/><text x="28" y="37" font-size="12" font-weight="700" fill="#fff" text-anchor="middle" font-family="Arial">$</text></svg>
  <div class="service-name">Mortage Refinance</div>
  <div class="service-text">Consolidate your debt into available home loan equity, signnifically reducing your general repayment</div>
</div>
<div class="service abs" style="left:486px;top:394px">
  <svg class="service-icon" viewBox="0 0 56 56"><circle cx="28" cy="28" r="27" fill="#1a3161" stroke="#cfd6e3" stroke-width="2"/><rect x="14" y="18" width="24" height="20" fill="none" stroke="#fff" stroke-width="2"/><path d="M18 23h16M18 27h16M18 31h12" stroke="#fff" stroke-width="1.6"/><path d="M34 34l9-9 2 2-9 9-3 1z" fill="#fff"/></svg>
  <div class="service-name">Debt Agreements</div>
  <div class="service-text">A viable alternative to bankruptcy and debt consolidtaions loans</div>
</div>

<div class="service abs" style="left:42px;top:561px">
  <svg class="service-icon" viewBox="0 0 56 56"><circle cx="28" cy="28" r="27" fill="#1a3161" stroke="#cfd6e3" stroke-width="2"/><path d="M16 26l10 14 14-24" fill="none" stroke="#fff" stroke-width="4"/><path d="M22 20v10M27 18v12M32 22v8" stroke="#fff" stroke-width="2.5"/></svg>
  <div class="service-name">Credit Repair</div>
  <div class="service-text">Assist you in removing unfair, disputable and incorrect information from your credit file / information, which you believe should not be there</div>
</div>
<div class="service abs" style="left:271px;top:561px">
  <svg class="service-icon" viewBox="0 0 56 56"><circle cx="28" cy="28" r="27" fill="#1a3161" stroke="#cfd6e3" stroke-width="2"/><rect x="16" y="24" width="5" height="16" fill="#fff"/><rect x="23" y="28" width="5" height="12" fill="#fff"/><rect x="30" y="32" width="5" height="8" fill="#fff"/><text x="38" y="26" font-size="13" font-weight="700" fill="#fff" text-anchor="middle" font-family="Arial">$</text><path d="M38 28v10M35 35l3 4 3-4" fill="none" stroke="#fff" stroke-width="1.6"/></svg>
  <div class="service-name">Bankruptcy</div>
  <div class="service-text">We will work with you yo accuartely determine if bankruptcy is the sole option of your situation</div>
</div>
<div class="service abs" style="left:486px;top:561px">
  <svg class="service-icon" viewBox="0 0 56 56"><circle cx="28" cy="28" r="27" fill="#1a3161" stroke="#cfd6e3" stroke-width="2"/><rect x="15" y="15" width="6" height="14" rx="1" fill="#fff"/><path d="M23 15h13c2 0 3 1 3 3l-2 10h-7l1 7c0 3-3 4-4 2l-4-10z" fill="#fff"/></svg>
  <div class="service-name">Bad Credit Loans</div>
  <div class="service-text">We Work in your best interests to provide a consilidtaion loan that turns yourbad credit history into a positive financial situation</div>
</div>

<section class="consult abs">
  <h2 class="consult-title abs" style="font-weight:400">Free Consultaion</h2>
  <div class="dash abs" style="left:295px;top:40px;width:152px;border-color:#cfe0b8"></div>
  <p class="consult-sub abs">Fill In The Form Below To Recieve Your Free, No Obligation Consulation</p>
  <div class="field abs" style="left:73px;top:78px">Name</div>
  <div class="field abs" style="left:271px;top:78px">Phone</div>
  <div class="field abs" style="left:468px;top:78px">Email</div>
  <div class="field abs" style="left:73px;top:102px">PostCode</div>
  <div class="field abs" style="left:271px;top:102px">Unsecured Debt.</div>
  <div class="field abs" style="left:468px;top:102px">Preferred Call Time</div>
  <a class="btn abs">GET MY FREE CONSTULATION</a>
</section>

<section class="reviews abs">
  <h2 class="reviews-title abs" style="font-weight:400">We Make Our Clients’ Happy</h2>
  <p class="reviews-sub abs">See What Our Say About us</p>
  <div class="dash abs" style="left:223px;top:60px;width:285px;border-color:#8796b3"></div>

  <svg class="abs" style="left:20px;top:128px" width="16" height="30" viewBox="0 0 16 30"><path d="M14 2L2 15l12 13" fill="none" stroke="#fff" stroke-width="1.6"/></svg>
  <svg class="abs" style="left:683px;top:128px" width="16" height="30" viewBox="0 0 16 30"><path d="M2 2l12 13L2 28" fill="none" stroke="#fff" stroke-width="1.6"/></svg>

  <svg class="avatar abs" style="left:50px;top:92px" viewBox="0 0 72 72" role="img" aria-label="Client portrait"><polygon points="36,2 66,19 66,53 36,70 6,53 6,19" fill="#c9c2bb" stroke="#fff" stroke-width="3"/></svg>
  <div class="quote abs" style="left:130px;top:86px"><span class="quote-mark">“</span>We were on the verge of losing our car &amp; did not know what to do, but now we are in an affordable arrangement to catch up our car payments and are on our way to a debt free future. We are even thinking of buying a house, without your help this would not be possible.</div>
  <div class="author abs" style="left:145px;top:188px">Joanne, Box Hill, VIC</div>

  <svg class="avatar abs" style="left:382px;top:92px" viewBox="0 0 72 72" role="img" aria-label="Client portrait"><polygon points="36,2 66,19 66,53 36,70 6,53 6,19" fill="#c9c2bb" stroke="#fff" stroke-width="3"/></svg>
  <div class="quote abs" style="left:462px;top:86px"><span class="quote-mark">“</span>We were on the verge of losing our car &amp; did not know what to do, but now we are in an affordable arrangement to catch up our car payments and are on our way to a debt free future. We are even thinking of buying a house, without your help this would not be possible.</div>
  <div class="author abs" style="left:477px;top:194px">Joanne, Box Hill, VIC</div>
</section>

<footer class="site-footer abs">
  <span>© 2015 ClearPathLedger. All Rights Reserved</span><span class="sep"></span><span>Privacy Policy</span><span class="sep"></span><span>Terms &amp; Conditions</span>
</footer>

</body>
</html>
```